PowerPoint Design Project

We are looking for a corporate presentation design (example content provided on approximately 30 slides).

The design will be a corporate design for our brand: GVRU
Continental Voyage Planners Union
For brand colours, requirements and logo look at: www.gvru-sample.org/media
or check the attached documents. We need to incorporate logo and brand but we are happy to refresh the palette. Attached please also find designs and colour palette of our new website-presentation should complement these.

You are also free to use photos from events some of which can be found here:
http://www.socialpage-example.com/pages/Continental-Voyage-Planners-Union/507194362810935?sk=photos_stream

Most important:
-PROFESSIONAL AUDIENCE-PROFESSIONAL DESIGN
-SIMPLE (see example our homepage in attachment)
-ADDED SIMPLE ANIMATIONS

-DESIGN TO BE DONE ON THE EXAMPLE PRESENTATION BUT TO BE RE-USABLE FOR OTHER PRESENTATIONS
Updates

Hi, we have just uploaded our corporate social media icons which could be added on contact/end slide and on the welcome slide.

Hi all, 

-I uploaded a new high res version of the map which can be included in your designs (feel free to change colour scheme)
-Also amended upload of the Google + social media icon

Reason: I am looking forward to seeing a couple more designs. Please try including some suggested animations.

Target Market(s)

Presentation will be B2B and most audience are representatives of various companies in the tourism industry (tour operators, tourist boards, hotels )

Industry/Entity Type

Events

Requirements
Must have
• sleek graphics design
Nice to have
• animations

```html
<!DOCTYPE html>
<html lang="en">
<head>
<meta charset="utf-8">
<title>GVRU Members: Buyers</title>
<link rel="stylesheet" href="https://fonts.googleapis.com/css2?family=Carlito:wght@400;700&display=swap">
<style>
  :root {
    --sidebar: #0f1736;
    --header-dark: #16264a;
    --header-light: #223c62;
    --page: #f7f7f8;
    --ink: #0c0c0c;
    --white: #ffffff;
    --mark-ink: #d9dce6;
    --partner-ink: #e08a12;
    --map-a: #f2f4f8;
    --map-b: #aab4c6;
  }
  * { margin: 0; padding: 0; box-sizing: border-box; }
  html, body { width: 1200px; height: 900px; overflow: hidden; }
  body { font-family: "Carlito", "Calibri", sans-serif; background: var(--page); }

  .slide { position: relative; width: 1200px; height: 900px; background: linear-gradient(180deg, #ffffff 0%, var(--page) 100%); }

  .sidebar { position: absolute; left: 0; top: 0; width: 160px; height: 900px; background: var(--sidebar); }

  .header {
    position: absolute; left: 160px; top: 0; right: 0; height: 138px;
    background: linear-gradient(90deg, var(--header-dark) 0%, var(--header-light) 100%);
  }
  .slide-title {
    position: absolute; left: 56px; top: 34px;
    color: var(--white); font-weight: 700; font-size: 48px; letter-spacing: 0.3px;
  }

  .brand-mark {
    position: absolute; left: 0; top: 50px; width: 160px; text-align: center;
    color: var(--mark-ink); font-weight: 400; font-size: 24px; letter-spacing: 1px;
  }
  .brand-mark .dot {
    display: block; width: 70px; height: 70px; margin: 0 auto 0;
    border: 2px solid var(--mark-ink); border-radius: 50%;
    position: absolute; left: 45px; top: -20px;
  }
  .brand-mark .name { position: relative; top: 4px; }

  .region-map {
    position: absolute; left: 1078px; top: 12px; width: 104px; height: 112px;
    background: radial-gradient(circle at 45% 50%, var(--map-a) 0%, var(--map-b) 100%);
    border-radius: 6px; opacity: 0.9;
  }

  .buyer-list { position: absolute; left: 276px; top: 300px; list-style: none; }
  .buyer-list li {
    display: flex; align-items: center; height: 104px;
    font-weight: 700; font-size: 43px; color: var(--ink);
  }
  .buyer-list svg { width: 38px; height: 38px; margin-right: 4px; flex: none; }

  .partner-badge {
    position: absolute; left: 25px; top: 802px; width: 122px; height: 48px;
    background: var(--white); display: flex; align-items: center; justify-content: center;
    color: var(--partner-ink); font-weight: 700; font-size: 20px;
  }
</style>
</head>
<body>
  <div class="slide">
    <aside class="sidebar">
      <div class="brand-mark"><span class="dot"></span><span class="name">GVRU</span></div>
      <div class="partner-badge">Tradeway</div>
    </aside>
    <header class="header">
      <h1 class="slide-title">GVRU Members: Buyers</h1>
    </header>
    <div class="region-map" role="img" aria-label="Dotted map of the continent"></div>

    <ul class="buyer-list">
      <li><svg viewBox="0 0 40 40" aria-hidden="true"><polygon points="4,4 36,20 4,36 12,20" fill="#111"/><polygon points="4,36 36,20 12,20" fill="#555"/></svg>Tour Operators</li>
      <li><svg viewBox="0 0 40 40" aria-hidden="true"><polygon points="4,4 36,20 4,36 12,20" fill="#111"/><polygon points="4,36 36,20 12,20" fill="#555"/></svg>Wholesalers</li>
      <li><svg viewBox="0 0 40 40" aria-hidden="true"><polygon points="4,4 36,20 4,36 12,20" fill="#111"/><polygon points="4,36 36,20 12,20" fill="#555"/></svg>Online Intermediaries</li>
      <li><svg viewBox="0 0 40 40" aria-hidden="true"><polygon points="4,4 36,20 4,36 12,20" fill="#111"/><polygon points="4,36 36,20 12,20" fill="#555"/></svg>MICE buyers</li>
    </ul>
  </div>
</body>
</html>
```